Childcare Centre trifold brochure

Design a contemporary trifold brochure for a childcare centre that meets Australian printing requirements with supplied content, logo's, fonts and photo's. Please refer to the attached DL flyer front and back for similar possible style and content.

Target Market(s)

Families

Industry/Entity Type

Childcare

Requirements
Must have
• refer attached content, photo's, logo's and examples. Colours should be same as Pantone purple and green and or variations of. Refer attached dl flyer example.

```html
<!DOCTYPE html>
<html lang="en">
<head>
<meta charset="utf-8">
<title>Bright Sprouts – Trifold Brochure</title>
<link rel="stylesheet" href="https://fonts.googleapis.com/css2?family=Open+Sans:wght@400;600;700;800&display=swap">
<style>
  :root{
    --purple:#a21fc2;
    --purple-deep:#8a14b0;
    --magenta:#d43fd2;
    --pink-soft:#f0b6f0;
    --green:#35c83a;
    --green-deep:#1fa52a;
    --sky:#c9f3f4;
    --ink:#3a3a3a;
    --white:#ffffff;
    --canvas:#e4e4e4;
  }
  *{box-sizing:border-box;margin:0;padding:0}
  html,body{width:893px;height:1200px;overflow:hidden;background:var(--canvas)}
  body{font-family:"Open Sans",Arial,sans-serif;color:var(--ink);position:relative}
  .spread{position:absolute;left:36px;width:820px;height:560px;overflow:hidden;background:var(--white);box-shadow:0 4px 14px rgba(0,0,0,.18)}
  .spread--outside{top:20px}
  .spread--inside{top:620px}
  .spread svg.art{position:absolute;inset:0;width:820px;height:560px}
  .copy{position:absolute;font-size:7.4px;line-height:1.45;text-align:justify}
  .copy p{margin-bottom:5px}
  .copy--light{color:var(--white)}
  .brand{position:absolute;display:flex;align-items:center;gap:6px;font-weight:800;color:var(--purple)}
  .brand__dot{width:14px;height:14px;border-radius:50%;background:var(--green)}
  .brand--cover{left:585px;top:36px;font-size:17px}
  .brand--back{left:320px;top:312px;font-size:11px;color:var(--white)}
  .brand--back .brand__dot{background:var(--purple);width:10px;height:10px}
  .contact{position:absolute;left:318px;top:346px;list-style:none;color:var(--white);font-size:7.6px}
  .contact li{display:flex;align-items:center;gap:10px;height:22px}
  .contact svg{width:11px;height:11px;flex:none}
  .award-strip{position:absolute;left:590px;top:352px;width:210px;transform:rotate(-10deg);transform-origin:left top;color:var(--purple-deep);font-size:7.5px;font-weight:600;text-align:center}
  .tagline{position:absolute;left:580px;top:395px;width:230px;transform:rotate(-10deg);transform-origin:left top;color:var(--white);font-size:13px;font-weight:700;line-height:1.25;text-align:center}
  .pull-quote{position:absolute;left:300px;top:440px;width:228px;padding:10px 14px;transform:rotate(-6deg);background:var(--pink-soft);box-shadow:-6px 7px 0 var(--purple);font-size:7.4px;line-height:1.45;color:var(--purple-deep);text-align:center;font-style:italic}
  .signature{position:absolute;left:690px;top:452px;font-size:12px;color:var(--white);font-style:italic;font-weight:600}
</style>
</head>
<body>

<section class="spread spread--outside" aria-label="Brochure outside">
  <svg class="art" viewBox="0 0 820 560">
    <defs>
      <linearGradient id="purpleBody" x1="0" y1="0" x2="0" y2="1">
        <stop offset="0" stop-color="#b62ad0"/><stop offset="1" stop-color="#8d16b5"/>
      </linearGradient>
      <linearGradient id="greenBody" x1="0" y1="0" x2="0" y2="1">
        <stop offset="0" stop-color="#3fd443"/><stop offset="1" stop-color="#25b02d"/>
      </linearGradient>
      <linearGradient id="woodland" x1="0" y1="0" x2="1" y2="1">
        <stop offset="0" stop-color="#6f6a3c"/><stop offset="1" stop-color="#3f4a2c"/>
      </linearGradient>
      <linearGradient id="meadow" x1="0" y1="0" x2="0" y2="1">
        <stop offset="0" stop-color="#9fd0f0"/><stop offset=".5" stop-color="#8fc25a"/><stop offset="1" stop-color="#5b9a2c"/>
      </linearGradient>
    </defs>

    <path role="img" aria-label="Photo: child in a purple hat exploring outdoors" fill="url(#woodland)" d="M0 0H273V260H0Z"/>
    <path fill="var(--white)" d="M0 232 Q140 282 273 222 V236 Q140 296 0 246Z"/>
    <path fill="url(#purpleBody)" d="M0 244 Q140 294 273 234 V560H0Z"/>

    <rect x="273" y="0" width="274" height="300" fill="var(--sky)"/>
    <path role="img" aria-label="Photo: children running across a grassy field" fill="url(#meadow)" d="M273 0H547V200 Q410 300 273 200Z"/>
    <path fill="url(#greenBody)" d="M273 210 Q410 310 547 210 V560H273Z"/>
    <circle cx="410" cy="232" r="52" fill="var(--green-deep)"/>
    <circle role="img" aria-label="Photo: children at play with craft materials" cx="410" cy="232" r="48" fill="#8c5a4a"/>

    <rect x="547" y="0" width="273" height="560" fill="var(--sky)"/>
    <path fill="var(--pink-soft)" d="M547 160 Q683 120 820 150 V330 H547Z" opacity=".6"/>
    <circle cx="683" cy="218" r="106" fill="var(--purple)"/>
    <circle role="img" aria-label="Photo: group of smiling children outdoors" cx="683" cy="218" r="101" fill="#d9a57f"/>
    <path fill="url(#purpleBody)" d="M547 340 L820 292 V560 H547Z"/>
    <path fill="var(--white)" d="M575 352 L805 312 L810 330 L580 370Z"/>
  </svg>

  <div class="copy copy--light" style="left:18px;top:292px;width:238px">
    <p>We are a Reggio Emilia inspired Childcare Centre offering long day care and a Nature Kindergarten program for 3 – 6 year olds.</p>
    <p>At the core of our program is a Child-First ‘emergent curriculum’. An emergent curriculum can be defined as a way of supporting learning that is based on the children’s interests.</p>
    <p>Learning occurs naturally, children thrive and learn best when their interests are considered and captured.</p>
    <p>Which means our Educators act as mentors for the children as they guide them through the adventure of learning outdoors in academic subjects such as science, technology, engineering and maths (STEM).</p>
    <p>Our children spend their days predominantly outdoors all year round in one of two amazing large Naturescape playgrounds full of native trees, a running creek bed, large stepping logs, a herb, vegetable and bush tucker garden along with a recycled mud kitchen made by the children, worm farm, compost bin and chickens and a fire pit where the older children can cook over an open fire.</p>
  </div>

  <div class="brand brand--back"><span class="brand__dot"></span>Bright Sprouts</div>
  <ul class="contact">
    <li><svg viewBox="0 0 12 12"><path fill="#fff" d="M3 1l2 2.5-1 1.2a6 6 0 003.3 3.3l1.2-1L11 9l-1 2C5 11 1 7 1 2z"/></svg>08 9000 1234</li>
    <li><svg viewBox="0 0 12 12"><circle cx="6" cy="6" r="5" fill="none" stroke="#fff"/><path d="M1 6h10M6 1c-3 3-3 7 0 10M6 1c3 3 3 7 0 10" fill="none" stroke="#fff" stroke-width=".8"/></svg>hello@brightsprouts.com.au</li>
    <li><svg viewBox="0 0 12 12"><rect x="1" y="2.5" width="10" height="7" fill="none" stroke="#fff"/><path d="M1 2.5l5 4 5-4" fill="none" stroke="#fff"/></svg>brightsprouts.com.au</li>
    <li><svg viewBox="0 0 12 12"><path fill="#fff" d="M6 1a3.5 3.5 0 013.5 3.5C9.5 7 6 11 6 11S2.5 7 2.5 4.5A3.5 3.5 0 016 1z"/><circle cx="6" cy="4.5" r="1.3" fill="var(--green)"/></svg>18 Banksia Road, Wattle Grove, WA 6107</li>
    <li style="height:28px"><svg viewBox="0 0 12 12"><circle cx="6" cy="6" r="5" fill="none" stroke="#fff"/><path d="M6 3v3.2l2 1.3" fill="none" stroke="#fff"/></svg><span>6:00am – 6:00pm Monday – Friday<br>(except public holidays)</span></li>
    <li><svg viewBox="0 0 12 12"><rect x="1.5" y="1.5" width="9" height="9" fill="#fff"/></svg>brightsproutsAU</li>
  </ul>

  <div class="brand brand--cover"><span class="brand__dot"></span>Bright Sprouts</div>
  <div class="award-strip">Finalist, Early Childhood Service of the Year, 2018</div>
  <div class="tagline">Proud Provider of High Quality Childcare Education and Learning Outcomes for Children</div>
</section>

<section class="spread spread--inside" aria-label="Brochure inside">
  <svg class="art" viewBox="0 0 820 560">
    <defs>
      <linearGradient id="purpleBody2" x1="0" y1="0" x2="0" y2="1">
        <stop offset="0" stop-color="#c63dd6"/><stop offset="1" stop-color="#8d16b5"/>
      </linearGradient>
      <linearGradient id="trail" x1="0" y1="0" x2="1" y2="1">
        <stop offset="0" stop-color="#9b8a6a"/><stop offset="1" stop-color="#5d5440"/>
      </linearGradient>
    </defs>
    <path fill="var(--sky)" d="M0 0H547V24 Q520 34 500 26 Q470 36 440 26 Q410 36 380 26 Q350 36 320 26 Q290 36 273 28 Q250 36 220 26 Q190 36 160 26 Q130 36 100 26 Q70 36 40 26 Q20 34 0 26Z"/>
    <path fill="var(--sky)" d="M0 540 Q40 528 80 540 Q120 528 160 540 Q200 528 240 540 Q280 528 320 540 Q360 528 400 540 Q440 528 480 540 Q510 528 547 540 V560 H0Z"/>
    <line x1="273" y1="0" x2="273" y2="560" stroke="#eee"/>

    <path fill="var(--purple)" d="M0 330 Q160 310 260 420 Q273 470 273 560 H0Z"/>
    <path role="img" aria-label="Photo: toddler in a purple hat playing in the dirt" fill="#a48f78" d="M0 338 Q155 320 252 424 Q265 470 265 560 H0Z"/>

    <path role="img" aria-label="Photo: children climbing along a log trail" fill="url(#trail)" d="M547 0H820V230 Q700 300 547 250Z"/>
    <path fill="var(--green)" d="M547 250 Q700 300 820 230 V240 Q700 310 547 260Z"/>
    <path fill="url(#purpleBody2)" d="M547 258 Q700 310 820 238 V560 H547Z"/>
    <circle cx="610" cy="260" r="52" fill="var(--green)"/>
    <circle role="img" aria-label="Photo: two young children lying on the grass" cx="610" cy="260" r="48" fill="#b9a07c"/>
    <path d="M615 484l4 9 9 1-7 6 2 9-8-5-8 5 2-9-7-6 9-1z" fill="#f2d42a"/>
    <rect x="640" y="490" width="52" height="24" fill="var(--white)" opacity=".85"/>
    <rect x="700" y="494" width="22" height="22" fill="#5b6cd0"/>
    <rect x="740" y="498" width="56" height="20" fill="var(--white)" opacity=".85"/>
  </svg>

  <div class="copy" style="left:22px;top:40px;width:230px">
    <p>The children are taught real life skills and do their own individual risk assessments before engaging in learning experiences such as crossing a flowing river creek bed, walking along logs, and climbing &amp; jumping off trees. They also learn whittling, lighting fires (using steel flints), use proper hand tools such as hacksaws, hammers and manual hand drills and learn how to navigate uneven terrain.</p>
    <p>The significant importance of learning through play while outdoors in a natural environment cannot be underestimated.</p>
    <p>Just as importantly the children are able to explore and play at their own pace and set their own rhythm.</p>
    <p>In relation to children’s wellbeing, long-term outdoor preschool programmes were found to have positive impacts on both children’s physical and mental health. The studies found that as well as promoting wellbeing in children, the programmes enhance their confidence and resilience, persistence and problem-solving skills.</p>
  </div>

  <div class="copy" style="left:292px;top:40px;width:236px">
    <p>Children’s confidence increased, and they had heightened levels of self-belief, positive attitude, independence and demonstrated an increased ability to take initiatives.</p>
    <p>Children who play regularly in natural settings are sick less often. Mud, sand, water, leaves, sticks, pine cones and gum nuts can help to stimulate children’s immune system as well as their imagination.</p>
    <p>Children who spend more time outside tend to be more physically active and are less likely to be overweight. They are more resistant to stress, have lower incidence of behavioural disorders, anxiety and depression, and have a higher measure of self-worth.</p>
    <p>Since 2015, throughout each school term our educators run free lessons for all ages in the following: yoga, meditation, sign language, Spanish, German, Malaysian, Sri Lankan Culture, Sustainability, Noongar Culture &amp; Sport.</p>
    <p>The sign language is a particular hit with the mothers as the babies are able to sign to their parents when they are hungry or need to go to the toilet before they even start talking.</p>
    <p>The first five years of a child’s development are the most crucial with 90% of their brain synapsis being formed by this time.</p>
    <p>Becoming multilingual or being able to sign has an exponential effect on the children’s development outcomes which is why we offer such a vast array of authentic learning experiences.</p>
  </div>

  <div class="pull-quote">“Early childhood is the most important time for brain development. It is the time in a child’s life where they start building their brain connections and therefore, ultimately, the work we do will shape their life forever.”</div>

  <div class="copy copy--light" style="left:568px;top:316px;width:232px">
    <p>“Providing outdoor opportunities for learning is a critical priority for parents, teachers and the wider community.” “Outdoor learning was added to the national curriculum in 2015, however just 34% of teachers surveyed taught outdoors for 15 minutes or more.” “Nature ignites passion, inspiration, creativity &amp; purpose and plays an important role in the cognitive, emotional and physical development of children.”</p>
    <p>“Passion is lifted from the earth itself by the muddy hands of the young; it travels along grass stained sleeves to the heart. If we are going to save environmentalism and the environment, we must also save an endangered indicator species: the child in nature.”</p>
  </div>
  <div class="signature">—Maya Thornton</div>
</section>

</body>
</html>
```